Law Firm Needs Brochure Redesign Using New Logo

We are a personal injury law firm that does auto injuries and other personal injury cases. We want a new brochure that has our updated logo and information. Instead of gold and black, we want more navy, as matches the new logo. The Auto Liability portion should read: "(required by the state of Arizona in the amounts of $25,000 per person / $50,000 per accident, but a higher amount may be best )." The other information can remain the same. We'd like the brochure to keep the same professional tone as the previous brochure.
Our website is https://www.marbrenlegal.com/.

```html
<!DOCTYPE html>
<html lang="en">
<head>
<meta charset="utf-8">
<title>Marbren Legal – Car Accident Brochure</title>
<link rel="stylesheet" href="https://fonts.googleapis.com/css2?family=Poppins:ital,wght@0,300;0,400;0,500;0,600;1,300&display=swap">
<style>
:root{
  --navy:#0f2343;
  --navy-deep:#0b1a33;
  --ink:#1b2a44;
  --gold:#c7ad7c;
  --gold-text:#d6b77a;
  --paper:#ffffff;
  --stage:#b9b9b9;
  --grey-text:#4a4f57;
}
*{box-sizing:border-box;margin:0;padding:0}
html,body{width:1200px;height:1200px;overflow:hidden}
body{background:var(--stage);font-family:"Poppins",sans-serif;color:var(--ink);position:relative}
.abs{position:absolute}
.side-label{position:absolute;font-weight:300;font-size:46px;letter-spacing:14px;color:var(--navy);white-space:nowrap}
.side-label.outside{left:190px;top:336px;transform:translate(-50%,-50%) rotate(-90deg)}
.side-label.inside{left:960px;top:870px;transform:translate(-50%,-50%) rotate(90deg)}

.spread{position:absolute;background:var(--paper);box-shadow:0 1px 3px rgba(0,0,0,.15)}
.outside-spread{left:233px;top:52px;width:677px;height:525px}
.inside-spread{left:233px;top:610px;width:680px;height:526px}

/* outside panel 1 */
.stats-photo{left:0;top:0;width:224px;height:312px;background:linear-gradient(180deg,#3a3433 0%,#24201f 45%,#121110 100%);color:#fff;text-align:center}
.stat-over{font-weight:300;font-size:16px;line-height:1}
.stat-num{font-weight:400;font-size:34px;line-height:1.05}
.stat-note{font-size:7px;line-height:1.3;padding:0 40px}
.stat-divider{width:64px;margin:10px auto;border-top:1px dashed rgba(255,255,255,.6)}
.promise{left:0;top:312px;width:224px;height:125px;background:var(--navy);color:#fff;font-size:10px;line-height:1.22;text-align:center;padding:13px 18px}
.brand{display:flex;align-items:center;gap:7px;color:var(--navy);font-weight:600;white-space:nowrap}
.brand-dot{width:14px;height:14px;border-radius:50%;background:var(--navy);flex:none}
.brand-name{font-size:17px;letter-spacing:1px;line-height:1;display:block}
.brand-sub{font-size:6.5px;letter-spacing:3px;font-weight:500;display:block;margin-top:3px}
.outside-logo-bottom{left:36px;top:460px}

/* outside panel 2 (mailer) */
.mailer{left:224px;top:0;width:226px;height:525px;background:linear-gradient(90deg,#eceff2 0%,#fff 30%)}
.mailer-return{left:32px;top:502px;transform:rotate(-90deg);transform-origin:left top;display:flex;flex-direction:column;align-items:flex-start;gap:6px;white-space:nowrap}
.mailer-return .brand{gap:6px}
.mailer-return .brand-name{font-size:13px}
.mailer-return .brand-sub{font-size:5.5px;letter-spacing:2.6px}
.mailer-address{font-size:7.2px;line-height:1.35;color:var(--ink);white-space:nowrap}

/* outside panel 3 (cover) */
.cover-logo{left:492px;top:30px}
.cover-photo{left:489px;top:83px;width:188px;height:388px;background:linear-gradient(160deg,#1f2a33 0%,#5d6a74 40%,#c9ced3 60%,#2c3238 100%)}
.cover-title{left:449px;top:311px;width:198px;height:125px;background:var(--navy);color:#fff;padding:15px 16px 0 20px;overflow:hidden}
.cover-title .light{font-weight:300;font-size:17px;line-height:1.18;letter-spacing:.2px;white-space:nowrap}
.cover-title .bold{font-weight:600;font-size:18px;line-height:1.2;white-space:nowrap}
.cover-title .tag{font-style:italic;font-weight:300;font-size:8.6px;line-height:1.45;margin-top:5px;white-space:nowrap}
.cover-url{left:449px;top:496px;width:228px;text-align:center;font-size:8px;letter-spacing:2.5px;color:var(--ink)}
.cover-url b{font-weight:600}

/* inside left panel */
.tips{left:0;top:0;width:229px;height:423px;background:linear-gradient(170deg,#13294d 0%,var(--navy-deep) 60%)}
.tips-tag{left:52px;top:16px;width:190px;height:46px}
.tips-tag-text{left:72px;top:22px;display:flex;align-items:center;gap:6px;color:var(--navy)}
.tips-top{font-weight:600;font-size:9px;line-height:1;text-align:center;border-right:1px solid var(--navy);padding-right:5px}
.tips-top span{display:block;font-size:22px;font-weight:500}
.tips-title{font-weight:500;font-size:14.5px;line-height:1.15}
.tips-list{left:20px;top:82px;width:204px;list-style:none;color:#fff;font-size:7.4px;line-height:1.25}
.tips-list li{position:relative;padding-left:10px;margin-bottom:9.2px}
.tips-list li::before{content:"";position:absolute;left:0;top:50%;border-left:3px solid #fff;border-top:2px solid transparent;border-bottom:2px solid transparent}
.tips-list em{font-style:normal;color:var(--gold-text)}
.crash-photo{left:0;top:423px;width:455px;height:103px;background:linear-gradient(90deg,#3f72b5 0%,#2b4c7d 35%,#6d6f73 55%,#1c1d20 100%)}

/* inside middle panel */
.cover-art{left:229px;top:0;width:226px;height:140px;background:radial-gradient(ellipse at 50% 60%,#f3f3f3 0%,#dcdcdc 70%,#cfcfcf 100%)}
.coverage-head{left:229px;top:140px;width:226px;height:25px;background:var(--navy);color:#fff;font-weight:500;font-size:14.5px;text-align:center;line-height:25px}
.coverage{left:245px;top:180px;width:205px;font-size:7.6px;line-height:1.2;color:var(--grey-text)}
.coverage h4{font-weight:600;color:var(--ink);font-size:7.6px;margin:10px 0 9px;padding-left:10px;position:relative}
.coverage h4::before{content:"";position:absolute;left:0;top:2px;border-left:3px solid var(--ink);border-top:2px solid transparent;border-bottom:2px solid transparent}

/* inside right panel */
.safety{left:472px;top:18px;width:200px}
.safety h3{font-weight:600;font-size:13px;color:var(--navy);padding-left:11px;position:relative;line-height:1.2}
.safety h3::before{content:"";position:absolute;left:0;top:6px;border-left:3px solid var(--navy);border-top:2px solid transparent;border-bottom:2px solid transparent}
.safety p{font-size:7.6px;line-height:1.2;color:var(--grey-text);margin-top:3px}
.safety p.strong{font-weight:600;color:var(--navy);margin-top:7px}
.road-photo{left:455px;top:164px;width:225px;height:204px;background:linear-gradient(150deg,#6c8a55 0%,#3f4a3a 45%,#181a1d 75%,#8d8a84 100%)}
.contact-bar{left:455px;top:368px;width:225px;height:35px}
.contact-bar-text{left:455px;top:368px;width:225px;height:35px;color:#fff;font-weight:500;font-size:15px;text-align:center;line-height:35px;padding-right:30px}
.contact{left:455px;top:420px;width:225px;text-align:center;font-size:11.2px;line-height:1.18;color:var(--ink)}
.contact b{font-weight:600;font-size:13.5px;color:var(--navy);display:block;margin-bottom:2px}
</style>
</head>
<body>

<div class="side-label outside">OUTSIDE</div>
<div class="side-label inside">INTSIDE</div>

<section class="spread outside-spread">
  <div class="abs stats-photo" role="img" aria-label="Dark photo of a child buckling a seat belt in a car seat">
    <div style="padding-top:120px">
      <div class="stat-over">over</div>
      <div class="stat-num">107,000</div>
      <div class="stat-note">crashes will happen in the state of Arizona this year.</div>
      <div class="stat-divider"></div>
      <div class="stat-over">over</div>
      <div class="stat-num">700</div>
      <div class="stat-note">of them will result in fatalities.</div>
    </div>
  </div>
  <div class="abs promise">If we don't win, you don't pay attorney fees. That seems fair to us. Know what's happening with your case, get the answers to your questions and work on getting better with the confidence that you've got an excellent group of people working for you.</div>
  <div class="abs brand outside-logo-bottom">
    <span class="brand-dot"></span>
    <span><span class="brand-name">MARBREN LEGAL</span><span class="brand-sub">INJURY LAWYERS</span></span>
  </div>

  <div class="abs mailer">
    <div class="abs mailer-return">
      <div class="brand">
        <span class="brand-dot" style="width:11px;height:11px"></span>
        <span><span class="brand-name">MARBREN LEGAL</span><span class="brand-sub">INJURY LAWYERS</span></span>
      </div>
      <div class="mailer-address">4820 E. Camelback Road Suite 310<br>Phoenix AZ 85018</div>
    </div>
  </div>

  <div class="abs brand cover-logo">
    <span class="brand-dot"></span>
    <span><span class="brand-name">MARBREN LEGAL</span><span class="brand-sub">INJURY LAWYERS</span></span>
  </div>
  <div class="abs cover-photo" role="img" aria-label="Car speeding through a lit tunnel with motion blur"></div>
  <div class="abs cover-title">
    <div class="light">PROTECT YOUR<br>FAMILY IN CASE OF</div>
    <div class="bold">A CAR ACCIDENT</div>
    <div class="tag">A little knowledge and preparation<br>go a long way</div>
  </div>
  <div class="abs cover-url">WWW.<b>MARBRENLEGAL</b>.COM</div>
</section>

<section class="spread inside-spread">
  <div class="abs tips">
    <svg class="abs tips-tag" viewBox="0 0 190 46" aria-hidden="true"><polygon points="14,0 190,0 190,46 14,46 0,23" fill="var(--gold)"/></svg>
    <div class="abs tips-tag-text">
      <div class="tips-top">TOP<span>10</span></div>
      <div class="tips-title">Tips to<br>Avoid a Crash</div>
    </div>
    <ul class="abs tips-list">
      <li><em>Anyone making a left turn must wait for all oncoming traffic to clear before proceeding.</em> Yes, even if the light has turned yellow. Wait to be sure that all traffic has stopped.</li>
      <li><em>When your light turns green,</em> check to be sure that no vehicles are entering the intersection late.</li>
      <li><em>Allow plenty of room between you and the car in front of you.</em> Traffic can stop in an instant, even if you can't see anything ahead.</li>
      <li><em>Avoid being distracted.</em> Teenagers are especially susceptible to losing focus if there are too many friends in the car.</li>
      <li><em>Keep the volume of your radio down and never wear headphones.</em> Cars are very soundproof these days, but you need to be able to hear an ambulance or police siren.</li>
      <li><em>Be especially careful on the weekends and early morning hours.</em></li>
      <li><em>Don't speed.</em> Speed is a factor in most crashes. Street lights are timed and the freeway has traffic. It's likely you won't get there much faster even if you do speed.</li>
      <li><em>Don't drink and drive.</em> Many cab companies offer a free service to get you home safe.</li>
      <li><em>Use your turn signals.</em> This gives an early warning to vehicles you may not be able to see.</li>
    </ul>
  </div>
  <div class="abs crash-photo" role="img" aria-label="Close-up of a blue car crashed into the rear of a black car"></div>

  <div class="abs cover-art" role="img" aria-label="Hands cupped protectively over a small silver toy car"></div>
  <div class="abs coverage-head">Have the Right Coverage</div>
  <div class="abs coverage">
    <p>Many people don't know about the different kinds of insurance available. In addition to health insurance, we suggest:</p>
    <h4>Auto Liability</h4>
    <p>(required by the state of Arizona in the amounts of $25,000 per person / $50,000 per accident, but a higher amount may be best ).</p>
    <h4>Uninsured or Underinsured Motorist Coverage.</h4>
    <p>This protects YOU when the other driver doesn't have insurance or not enough.</p>
    <h4>Medical Payments Coverage.</h4>
    <p>Up to $5,000 in coverage will be paid out to you no matter who is at fault in an accident and does not need to be reimbursed.</p>
    <h4>Homeowners / Renters Insurance.</h4>
    <p>Protects you in case of injuries on your property as well as damage to your home from covered events</p>
  </div>

  <div class="abs safety">
    <h3>Model Safe Behavior</h3>
    <p>Always buckle up. Always put your children in car seats/boosters that are rated for their height and weight.</p>
    <h3 style="margin-top:16px">Never Text While Driving</h3>
    <p>Studies have shown that texting while driving is as dangerous as driving intoxicated.</p>
    <p class="strong">Show your children that no text is more important than your safety. It can wait.</p>
  </div>
  <div class="abs road-photo" role="img" aria-label="Distressed driver leaning out of a car after a roadside collision"></div>
  <svg class="abs contact-bar" viewBox="0 0 225 35" overflow="visible" aria-hidden="true">
    <polygon points="0,0 225,0 225,35 122,35 113,43 104,35 0,35" fill="var(--navy)"/>
  </svg>
  <div class="abs contact-bar-text">Contact Us</div>
  <div class="abs contact">
    <b>Marbren Legal Group</b>
    4820 E. Camelback Road Suite 310<br>
    Phoenix AZ 85018<br>
    602.555.0147<br>
    info@MarbrenLegal.com<br>
    MarbrenLegal.com
  </div>
</section>

</body>
</html>
```